TRADE SHOW DISPLAY BANNER Design Project

Looking for a designer to use some photos (that i have taken), edit, cut out, and design a banner for a trade show display that i will be using at an expo.

The approx visible size will be: 295cm wide x 230cm high
(please view display size 1 - for sizes, and display size 2 - for display end product)

Industry/Entity Type

Trade

Requirements
Must have
• - main focus is the steel fence post. will require a picture of the fence with the posts,
photos for this point are ( fence2, fence 3, fence 4, fence 5, fence1 original, fence1)

- the 3 pictures, outlining how the brackets work. on the side
photos for this point are (steel post 1, steel post 2, steel post 3)

Will require 'STEEL FENCE POST' written somewhere on top in large letters. will also require the website written somewhere on the add - 'www.BrindleRailWorks.com.au'

Will requite the orlevy timber logo somewhere on the bottom corners of the add.
photo of this add is - 'orlevy timber logo'

the exact dimensions of the add can be seen in 'display size1'
the end product of the add will look like 'display size2'

```html
<!DOCTYPE html>
<html lang="en">
<head>
<meta charset="utf-8">
<title>Steel Fence Post – Trade Show Banner</title>
<link rel="stylesheet" href="https://fonts.googleapis.com/css2?family=Roboto+Condensed:wght@400;700&family=Open+Sans:wght@400;700&display=swap">
<style>
  :root {
    --teal: #12a196;
    --teal-light: #8fd1c7;
    --navy: #16153a;
    --navy-text: #2b2160;
    --white: #ffffff;
    --wood-light: #cdb48f;
    --wood-mid: #a98c66;
    --steel: #9ea4a8;
    --sky: #6a9fd6;
  }
  * { margin: 0; padding: 0; box-sizing: border-box; }
  html, body { width: 1200px; height: 960px; overflow: hidden; background: var(--teal); }
  .banner {
    position: relative;
    width: 1200px;
    height: 960px;
    background: var(--teal);
    font-family: "Roboto Condensed", "Arial Narrow", sans-serif;
  }
  .band-mid {
    position: absolute; left: 0; top: 247px; width: 1200px; height: 234px;
    background: var(--navy);
  }
  .band-foot {
    position: absolute; left: 0; top: 837px; width: 1200px; height: 123px;
    background: var(--navy);
  }
  .headline, .tagline, .subline {
    position: absolute; left: 0; top: 0; overflow: visible;
  }
  .headline text {
    font-family: "Roboto Condensed", "Arial Narrow", sans-serif;
    font-weight: 400; fill: var(--teal-light);
  }
  .tagline text {
    font-family: "Roboto Condensed", "Arial Narrow", sans-serif;
    font-weight: 700; fill: var(--white);
  }
  .subline text {
    font-family: "Roboto Condensed", "Arial Narrow", sans-serif;
    font-weight: 700; fill: var(--navy-text);
  }
  .fence-photo {
    position: absolute; top: 183px; width: 248px; height: 354px;
    border: 3px solid var(--white); border-radius: 4px;
    box-shadow: 5px 6px 10px rgba(0,0,0,0.45);
  }
  .fence-photo.one   { left: 66px;  background: linear-gradient(90deg, var(--steel) 0 14%, var(--wood-light) 14% 100%); }
  .fence-photo.two   { left: 335px; background: linear-gradient(180deg, var(--sky) 0 25%, #d9cbb4 25% 35%, var(--wood-light) 35% 88%, #6b5a45 88%); }
  .fence-photo.three { left: 610px; background: linear-gradient(90deg, var(--wood-mid) 0 68%, #b7bcc0 68% 92%, var(--wood-mid) 92%); }
  .fence-photo.four  { left: 884px; background: linear-gradient(90deg, #b09a7c 0 55%, #c9b594 55% 85%, #8f969b 85%); }
  .bracket-photo {
    position: absolute; top: 686px; width: 170px; height: 139px;
    border: 2px solid var(--navy);
    background: linear-gradient(180deg, #f4f4f4 0 38%, #b99d73 38% 74%, #f4f4f4 74%);
  }
  .bracket-photo.one   { left: 68px; }
  .bracket-photo.two   { left: 248px; background: linear-gradient(90deg, #f4f4f4 0 15%, #7f8589 15% 85%, #f4f4f4 85%); }
  .bracket-photo.three { left: 432px; }
  .website {
    position: absolute; left: 71px; top: 852px;
    font-family: "Open Sans", Arial, sans-serif; font-weight: 400;
    font-size: 45px; color: var(--white); letter-spacing: -0.3px;
    white-space: nowrap;
  }
  .brand {
    position: absolute; left: 763px; top: 790px; width: 365px;
    display: flex; align-items: center; justify-content: center; gap: 14px;
  }
  .brand-mark { width: 26px; height: 26px; background: var(--white); }
  .brand-name {
    font-family: "Roboto Condensed", "Arial Narrow", sans-serif;
    font-weight: 700; font-size: 58px; color: var(--white);
    text-transform: uppercase; white-space: nowrap; line-height: 1;
  }
</style>
</head>
<body>
  <main class="banner">
    <div class="band-mid"></div>
    <div class="band-foot"></div>

    <svg class="headline" width="1200" height="200" viewBox="0 0 1200 200">
      <text x="61" y="149" font-size="150" textLength="1085" lengthAdjust="spacingAndGlyphs">STEEL FENCE POST</text>
    </svg>

    <div class="fence-photo one" role="img" aria-label="Timber paling fence with a slim galvanised steel post at its end"></div>
    <div class="fence-photo two" role="img" aria-label="Long timber fence with steel posts alongside a house"></div>
    <div class="fence-photo three" role="img" aria-label="Close-up of a galvanised steel fence post with a black cap beside timber palings"></div>
    <div class="fence-photo four" role="img" aria-label="Corner of a timber fence fixed to steel posts with brackets"></div>

    <svg class="tagline" width="1200" height="700" viewBox="0 0 1200 700">
      <text x="66" y="642" font-size="88" textLength="1069" lengthAdjust="spacingAndGlyphs">SLIM, LIGHTWEIGHT &amp; DURABLE</text>
    </svg>
    <svg class="subline" width="1200" height="720" viewBox="0 0 1200 720">
      <text x="674" y="700" font-size="55" textLength="465" lengthAdjust="spacingAndGlyphs">The Timber Alternative</text>
    </svg>

    <div class="bracket-photo one" role="img" aria-label="Steel post bracket holding a timber rail, front view"></div>
    <div class="bracket-photo two" role="img" aria-label="Inside view of the steel post showing the bracket bolt"></div>
    <div class="bracket-photo three" role="img" aria-label="Bracket clipped onto the steel post with timber rail, angled view"></div>

    <div class="brand">
      <span class="brand-mark"></span>
      <span class="brand-name">Orlevy Timber</span>
    </div>

    <p class="website">www.BrindleRailWorks.com.au</p>
  </main>
</body>
</html>
```